Poster design for Workbay industrial Employment Solutions. "if the hat fits - wear it!"

Workbay is proud to be New Zealand owned and operated. We have an extensive branch network stretching from Queenstown to Auckland. While we are a nationwide company, we see ourselves as being local in every market, that’s what sets us aside from other temp agencies.

We are an industrial employment solutions company. We fined jobs for people in industries such as construction, roading, engineering, welding, painting, plumbing, warehousing, driving, logistics etc.

Our mission: 'Cool and easy' – at Workbay we are passionate about providing industrial employment solutions through consistent action in a positive, fun & innovative environment.
www.workbay-example.co.nz

Goal: To design a poster (size A1) that will draw target audience’s attention to it and make them want to call Workbay to get a job.

The design should be eye catchy and reflect “cool and easy” brand personality.

Target audience: Construction workers, labourers, engineers, drivers, plumbers, welders, builders, painters etc.

Text on the poster:

If the hat fits – wear it!
We can get you working sooner than anyone else.
We have jobs that need to be filled.
Call us NOW on 0508 73 73 73

Target Market(s)

people of blue colour professions (refer to the description)

Industry/Entity Type

Industrial

Requirements
Must have
• hard hat

```html
<!DOCTYPE html>
<html lang="en">
<head>
<meta charset="utf-8">
<title>Workbay – If the hat fits, wear it!</title>
<link rel="stylesheet" href="https://fonts.googleapis.com/css2?family=Oswald:wght@300;400;500;700&display=swap">
<style>
  :root {
    --blue: #1d3f93;
    --ink: #2b2b2b;
    --grey-text: #4a4a4a;
    --bar: #3f3f3f;
    --bg-top: #ffffff;
    --bg-bottom: #e4e5e7;
    --hat-light: #7a4d2b;
    --hat-dark: #4a2c16;
    --rule: #c9b59a;
  }
  html, body {
    margin: 0;
    padding: 0;
    overflow: hidden;
  }
  .poster {
    position: relative;
    width: 849px;
    height: 1200px;
    overflow: hidden;
    background: linear-gradient(180deg, var(--bg-top) 0%, #f4f4f5 45%, var(--bg-bottom) 100%);
    font-family: "Oswald", "Arial Narrow", sans-serif;
  }
  .brand {
    position: absolute;
    top: 23px;
    right: 28px;
    width: 264px;
    height: 62px;
    background: var(--blue);
    display: flex;
    align-items: center;
    justify-content: center;
  }
  .brand-name {
    color: #ffffff;
    font-weight: 700;
    font-size: 34px;
    letter-spacing: 2px;
    text-transform: uppercase;
  }
  .hat-photo {
    position: absolute;
    left: 99px;
    top: 127px;
    width: 651px;
    height: 368px;
    background: linear-gradient(180deg, var(--hat-light) 0%, #623c1f 60%, var(--hat-dark) 100%);
  }
  .headline {
    position: absolute;
    left: 113px;
    top: 693px;
    margin: 0;
    color: var(--ink);
    font-weight: 500;
    font-size: 55px;
    line-height: 110px;
    white-space: nowrap;
  }
  .headline .key {
    color: var(--blue);
    font-weight: 700;
    font-size: 110px;
  }
  .rule {
    position: absolute;
    left: 113px;
    top: 835px;
    width: 637px;
    height: 2px;
    background: linear-gradient(90deg, var(--rule), #e0d3c0 70%, transparent);
  }
  .promise {
    position: absolute;
    left: 113px;
    top: 846px;
    margin: 0;
    color: var(--grey-text);
    font-weight: 400;
    font-size: 34px;
    line-height: 1.3;
  }
  .jobs-bar {
    position: absolute;
    left: 113px;
    top: 966px;
    display: flex;
    align-items: center;
    gap: 18px;
  }
  .jobs-bar p {
    margin: 0;
    height: 54px;
    padding: 0 14px;
    background: var(--bar);
    color: #ffffff;
    font-weight: 500;
    font-size: 31px;
    line-height: 54px;
    white-space: nowrap;
  }
  .jobs-bar .accent {
    width: 12px;
    height: 54px;
    background: var(--blue);
  }
  .call {
    position: absolute;
    left: 113px;
    top: 1050px;
    margin: 0;
    color: var(--grey-text);
  }
  .call-label {
    display: block;
    font-weight: 400;
    font-size: 34px;
    line-height: 1.25;
  }
  .call-number {
    display: block;
    color: var(--blue);
    font-weight: 500;
    font-size: 56px;
    line-height: 1.15;
    letter-spacing: 1px;
  }
</style>
</head>
<body>
  <main class="poster">
    <div class="brand"><span class="brand-name">Workbay</span></div>

    <div class="hat-photo" role="img" aria-label="Photograph of a brown work hat with a braided band"></div>

    <h1 class="headline">If the <span class="key">HAT</span> fits - wear <span class="key">IT</span>!</h1>
    <div class="rule"></div>

    <p class="promise">We can get you working sooner<br>than anyone else.</p>

    <div class="jobs-bar">
      <p>We have jobs that need to be filled.</p>
      <span class="accent"></span>
    </div>

    <p class="call">
      <span class="call-label">Call us NOW on</span>
      <span class="call-number">0508 73 73 73</span>
    </p>
  </main>
</body>
</html>
```